Web Portal Design for Keltavo – Subcontractor Verification Platform

Keltavo is a European startup focused on verifying and confirming the identity of subcontractors in the transport and logistics industry to prevent fraud.
The platform’s main functions include:
Company verification – confirming the legitimacy and registration details of transport companies.
Identity verification – authenticating the identity of the person registering the company and associated drivers.
Geo-zone monitoring – a unique mobile feature that allows the creation of geo-fenced areas at loading locations. This enables verification and tracking of who is actually present and authorized to collect the goods.
Safe subcontracting visibility – full transparency of subcontracting chains, ensuring each level of cooperation remains verified and secure.
In short, Keltavo helps build secure subcontractor networks for both shippers and freight forwarders.
I have already created a basic website using Framer, but I am not fully satisfied with the current design and graphic quality. I’m looking for a professional designer who can help improve the UI/UX, visual consistency, and overall aesthetics of the portal to better reflect our innovative and security-focused mission.
Design Style & Colors:
Modern, minimalistic layout
Primary colors: gray, white, and black
Accent color: green (for highlights, buttons, and trust indicators)
Clean typography and intuitive structure
Preference for a professional, tech-oriented look that conveys trust, security, and innovation
The website must definitely include the option to book a demo and provide information about pricing models, which should be easy to edit. There should also be an option to purchase subscriptions directly through the website. There will be three pricing models.
My project should serve as your inspiration, not a template — I’m not expecting it to look identical. We’re looking for something unique and truly “wow.”
Updates
Low design quality
We are looking for a contractor to design and develop a website for the modern application Keltavo, focused on identity verification in the logistics and transport industry. The website will serve as a branding and sales tool, presenting the innovation, security, and professionalism of our solution.
We are not interested in ready-made templates – we expect a fully custom, unique design tailored to the nature of the product and the TSL market.
Keltavo is an advanced platform for verifying the identity of companies, drivers, and subcontractors in logistics. Our goal is to eliminate fraud, theft, and impersonation of legitimate carriers through:
digital identity verification
subcontractor authorisation
creation of trusted company lists
increasing supply chain security
The website should clearly communicate: security, technology, trust, and innovation.
Design Requirements
Style & Design
No ready-made templates
Modern, technology-driven appearance
Premium / corporate-tech aesthetic
Minimalist, clean layout with clear content hierarchy
Colour Scheme
Existing graphics in green tones (we provide our own materials)
Website background: grey or dark (graphite, dark anthracite, deep grey)
Contrasting elements for CTAs and key sections
Industry Focus
Logistics / Transport / Digital Security
Visual identity should evoke:
trust
control
technology
data protection
The website must allow:
easy content editing
independent updating of texts and images without developer involvement
full responsiveness (desktop, tablet, mobile)
fast loading performance
SEO-ready structure
Target Market(s)
Producers
Coding
Number of Pages Required
1 page
Look and feel

```html
<!DOCTYPE html>
<html lang="en">
<head>
<meta charset="utf-8">
<title>Keltavo – Verification Intelligence for Secure Logistics</title>
<link href="https://fonts.googleapis.com/css2?family=Inter:wght@400;500;600;700&display=swap" rel="stylesheet">
<style>
:root{
  --board:#b3b3b3;
  --white:#ffffff;
  --soft:#f5f6f8;
  --ink:#141a2b;
  --text:#1b2030;
  --muted:#5d6473;
  --green:#22b573;
  --green-soft:#e6f6ee;
  --navy:#131a2a;
  --navy-card:#1c2334;
  --line:#e5e8ec;
}
*{box-sizing:border-box;margin:0;padding:0}
html,body{width:1200px;height:1200px;overflow:hidden;background:var(--board);font-family:'Inter',sans-serif;color:var(--text)}
.board{position:absolute;left:0;top:0;width:1932px;height:1932px;transform:scale(.62112);transform-origin:0 0}
.page{position:absolute;background:var(--white);overflow:hidden;box-shadow:0 2px 8px rgba(0,0,0,.08)}
.page--home{left:218px;top:50px;width:693px;height:1835px}
.page--pricing{left:981px;top:51px;width:694px;height:1039px}
.abs{position:absolute}
.btn{position:absolute;display:flex;align-items:center;justify-content:center;font-weight:600;border-radius:2px}
.btn--green{background:var(--green);color:#fff}
.btn--outline{border:1.5px solid var(--ink);color:var(--ink);background:#fff}
.center{left:0;right:0;text-align:center}
.eyebrow{font-size:7px;font-weight:600;letter-spacing:.8px;color:var(--green)}
.h2{font-size:20px;font-weight:700;color:var(--ink);letter-spacing:-.2px}
.lead{font-size:8.5px;line-height:14.5px;color:var(--muted)}

/* nav */
.nav{left:0;top:0;width:693px;height:42px;background:#fff;box-shadow:0 1px 4px rgba(0,0,0,.06);z-index:2}
.logo{font-size:14px;font-weight:700;color:var(--ink)}
.nav__links{left:364px;top:16px;display:flex;gap:16px;font-size:7.5px;font-weight:500;color:var(--ink)}
/* hero */
.hero{left:0;top:42px;width:693px;height:348px;background:var(--soft)}
.badge{left:53px;top:56px;width:115px;height:15px;border-radius:8px;background:var(--green-soft);color:var(--green);font-size:6px;font-weight:600;display:flex;align-items:center;justify-content:center}
.hero__title{left:53px;top:84px;font-size:26.5px;line-height:29px;font-weight:700;letter-spacing:-.4px;color:var(--ink)}
.hero__text{left:53px;top:155px;width:260px;font-size:9.3px;line-height:15.7px;color:var(--muted)}
/* stats */
.stats{left:0;top:390px;width:693px;height:138px;display:flex;padding:0 46px}
.stat{flex:1;text-align:center;padding-top:48px}
.stat__num{font-size:21px;font-weight:700;color:var(--green)}
.stat__label{font-size:7px;color:var(--muted);margin-top:9px}
/* quotes */
.quotes{left:0;top:528px;width:693px;height:178px;background:var(--navy)}
.quote{top:42px;width:284px;height:95px;background:var(--navy-card);border-radius:3px;padding:18px 20px}
.quote__mark{font-size:18px;line-height:10px;color:#2e6e55;font-weight:700}
.quote__text{font-size:9.3px;line-height:16px;color:#fff;margin-top:0}
.quote__by{font-size:6.8px;color:#b7bcc8;margin-top:10px}
/* features */
.features{left:0;top:706px;width:693px;height:634px;background:#fff}
.card{position:absolute;width:184px;height:195px;background:#fff;border-top:2px solid var(--green);box-shadow:0 1px 5px rgba(0,0,0,.1);border-radius:2px;padding:21px 20px}
.card__icon{width:31px;height:30px;border-radius:3px;background:var(--green-soft);display:flex;align-items:center;justify-content:center}
.card__title{font-size:11.3px;line-height:18px;font-weight:700;color:var(--ink);margin-top:12px}
.card__text{font-size:7.7px;line-height:13px;color:var(--muted);margin-top:6px}
/* process */
.process{left:0;top:1340px;width:693px;height:458px;background:var(--soft)}
.step{left:53px;width:290px}
.step__num{position:absolute;left:0;top:0;width:20px;height:20px;border-radius:50%;background:var(--green);color:#fff;font-size:7.5px;font-weight:600;display:flex;align-items:center;justify-content:center}
.step__title{margin-left:33px;font-size:9.5px;font-weight:700;color:var(--ink);padding-top:1px}
.step__text{margin-left:33px;font-size:7.6px;line-height:13px;color:var(--muted);margin-top:5px}
.profile{left:365px;top:183px;width:280px;height:219px;background:#fff;border-radius:4px;box-shadow:0 1px 6px rgba(0,0,0,.08)}
.profile__head{left:16px;top:16px;width:248px;height:36px;border-bottom:1px solid var(--line)}
.profile__ico{left:0;top:2px;width:24px;height:24px;border-radius:3px;background:#e9ebef}
.profile__name{left:34px;top:2px;font-size:8px;line-height:13px;font-weight:600;color:var(--ink)}
.chip{right:0;top:0;width:38px;height:22px;border-radius:11px;background:var(--green-soft);color:var(--green);font-size:6.5px;display:flex;align-items:center;justify-content:center}
.cell{width:118px;height:63px;background:var(--soft);border-radius:3px;padding:11px 10px}
.cell__label{font-size:6.5px;font-weight:600;letter-spacing:.5px;color:var(--muted)}
.cell__val{font-size:7.8px;line-height:13px;font-weight:600;color:var(--ink);margin-top:6px}

/* pricing */
.plan{position:absolute;background:#fff;border-radius:3px;box-shadow:0 1px 6px rgba(0,0,0,.1);text-align:center}
.plan--featured{border:1.5px solid var(--green)}
.plan__pop{left:62px;top:-5px;width:70px;height:14px;border-radius:7px;background:var(--green);color:#fff;font-size:6px;font-weight:600;display:flex;align-items:center;justify-content:center}
.plan__name{font-size:11px;font-weight:600;color:var(--ink)}
.plan__price{font-size:21px;font-weight:700;color:var(--ink);margin-top:12px}
.plan__per{font-size:6.8px;color:var(--muted);margin-top:8px}
.plan__list{list-style:none;text-align:left;margin-top:18px;padding-left:19px}
.plan__list li{font-size:7.8px;color:var(--ink);height:21.3px;display:flex;align-items:flex-start;gap:8px}
.plan__list li span.tick{color:var(--green);font-size:7px}
.plan__list li span.cross{color:#aeb3bc;font-size:7px}
.cta{left:68px;top:549px;width:559px;height:219px;border-radius:5px;background:linear-gradient(120deg,#1a2233,#2d374b)}
.footer{left:0;top:818px;width:694px;height:221px;background:var(--navy);color:#fff}
.f-title{font-size:9.5px;font-weight:600}
.f-rule{width:18px;height:1.5px;background:var(--green);margin-top:6px}
.f-list{list-style:none;margin-top:14px;font-size:7.3px;color:#aab0bd}
.f-list li{height:19.5px}
.social{width:19px;height:19px;border-radius:50%;background:#3a4152}
</style>
</head>
<body>
<div class="board">

  <!-- Home page -->
  <div class="page page--home">
    <header class="abs nav">
      <div class="abs logo" style="left:53px;top:13px">Keltavo</div>
      <nav class="abs nav__links"><span>Features</span><span>How It Works</span><span>Pricing</span><span>About</span></nav>
      <div class="btn btn--green" style="left:571px;top:12px;width:74px;height:18px;font-size:7px;font-weight:500">Book a Demo</div>
    </header>

    <section class="abs hero">
      <svg class="abs" style="left:0;top:0" width="693" height="348"><polygon points="440,0 693,0 693,126" fill="#e6efeb"/></svg>
      <div class="abs badge">Trusted transport starts here</div>
      <h1 class="abs hero__title">Verification Intelligence<br>for Secure Logistics</h1>
      <p class="abs hero__text">At Keltavo, we're building a new standard for security and verification in logistics — creating an environment where every connection is verified, every process is transparent, and every partner can operate with complete confidence.</p>
      <div class="btn btn--green" style="left:53px;top:253px;width:86px;height:29px;font-size:8px">Start for free</div>
      <div class="btn btn--outline" style="left:150px;top:253px;width:104px;height:29px;font-size:8px">See how it works</div>
    </section>

    <section class="abs stats">
      <div class="stat"><div class="stat__num">99.9%</div><div class="stat__label">Verification Accuracy</div></div>
      <div class="stat"><div class="stat__num">5,000+</div><div class="stat__label">Verified Companies</div></div>
      <div class="stat"><div class="stat__num">15,000+</div><div class="stat__label">Authorized Drivers</div></div>
      <div class="stat"><div class="stat__num">€100M+</div><div class="stat__label">Cargo Protected</div></div>
    </section>

    <section class="abs quotes">
      <div class="abs quote" style="left:53px"><div class="quote__mark">"</div><p class="quote__text">Don't risk €100,000 of cargo for €200 margin</p><p class="quote__by">— Logistics Security Expert</p></div>
      <div class="abs quote" style="left:361px"><div class="quote__mark">"</div><p class="quote__text">Are you a freight forwarder? Prove your resources are safe</p><p class="quote__by">— Industry Best Practice</p></div>
    </section>

    <section class="abs features">
      <div class="abs center eyebrow" style="top:52px">PLATFORM FEATURES</div>
      <h2 class="abs center h2" style="top:73px">All your verification tools in one simple platform</h2>
      <p class="abs center lead" style="top:114px;left:170px;right:170px">Subcontracting doesn't have to be risky – it can open up new opportunities. Create the perfect mix of tools to protect your business.</p>

      <div class="card" style="left:53px;top:176px">
        <div class="card__icon"><svg width="14" height="12" viewBox="0 0 14 12" fill="none" stroke="#22b573" stroke-width="1.4"><rect x="5" y="1" width="4" height="3"/><rect x="1" y="8" width="4" height="3"/><rect x="9" y="8" width="4" height="3"/><path d="M7 4v2H3v2M7 6h4v2"/></svg></div>
        <div class="card__title">Your Unique Network</div>
        <p class="card__text">Create and manage your own network of verified partners — carriers, drivers, and loading points. Control who gains access to your operations.</p>
      </div>
      <div class="card" style="left:257px;top:176px">
        <div class="card__icon"><svg width="10" height="13" viewBox="0 0 10 13"><path d="M5 0a5 5 0 0 1 5 5c0 4-5 8-5 8S0 9 0 5a5 5 0 0 1 5-5z" fill="#22b573"/><circle cx="5" cy="5" r="1.8" fill="#e6f6ee"/></svg></div>
        <div class="card__title">Smart Access &amp; Location</div>
        <p class="card__text">Access to loading sites is granted only after a verified driver enters the defined geo-zone. Create fixed or custom zones for each order.</p>
      </div>
      <div class="card" style="left:461px;top:176px">
        <div class="card__icon"><svg width="14" height="10" viewBox="0 0 14 10"><path d="M7 0C3 0 0 5 0 5s3 5 7 5 7-5 7-5-3-5-7-5z" fill="#22b573"/><circle cx="7" cy="5" r="2" fill="#e6f6ee"/></svg></div>
        <div class="card__title">No Hidden<br>Subcontracting</div>
        <p class="card__text">Even if your choice is passed along the chain, we give you full visibility of who actually executes the job — with instant issue notifications.</p>
      </div>
      <div class="card" style="left:53px;top:392px">
        <div class="card__icon"><svg width="15" height="12" viewBox="0 0 15 12"><circle cx="5" cy="3" r="3" fill="#22b573"/><path d="M0 12c0-4 2-5 5-5s5 1 5 5z" fill="#22b573"/><circle cx="12" cy="9" r="2.5" fill="none" stroke="#22b573" stroke-width="1.2"/></svg></div>
        <div class="card__title">You Know Who You Work<br>With</div>
        <p class="card__text">Verifies every company, employee, and driver through a secure, AI-powered process. Work only with trusted partners verified in minutes.</p>
      </div>
      <div class="card" style="left:257px;top:392px">
        <div class="card__icon"><svg width="14" height="12" viewBox="0 0 14 12"><path d="M0 4L7 0l7 4v8H0z" fill="#22b573"/><path d="M3 6h8M3 8h8M3 10h8" stroke="#e6f6ee" stroke-width="1"/></svg></div>
        <div class="card__title">Loading Gate<br>Management</div>
        <p class="card__text">Automate the entire loading access process. No longer need to manually identify and check documents at gate operations.</p>
      </div>
      <div class="card" style="left:461px;top:392px">
        <div class="card__icon"><svg width="13" height="12" viewBox="0 0 13 12" stroke="#22b573" stroke-width="1.2" fill="#e6f6ee"><path d="M0 2h13M0 6h13M0 10h13"/><circle cx="4" cy="2" r="1.5"/><circle cx="9" cy="6" r="1.5"/><circle cx="5" cy="10" r="1.5"/></svg></div>
        <div class="card__title">Automated Verification</div>
        <p class="card__text">Turn complex verification processes into smooth, automated workflows. Work smarter, safer and faster than ever before.</p>
      </div>
    </section>

    <section class="abs process">
      <div class="abs center eyebrow" style="top:52px">HOW IT WORKS</div>
      <h2 class="abs center h2" style="top:73px">Streamlined Verification Process</h2>
      <p class="abs center lead" style="top:115px;left:180px;right:180px">Our AI-powered platform transforms complex verification into a seamless, automated workflow.</p>

      <div class="abs step" style="top:176px"><div class="step__num">1</div><div class="step__title">Company Verification</div><p class="step__text">We verify company registration details, financial stability, and operational history to ensure legitimacy.</p></div>
      <div class="abs step" style="top:238px"><div class="step__num">2</div><div class="step__title">Identity Authentication</div><p class="step__text">Authenticate the identity of company representatives and drivers with advanced document verification.</p></div>
      <div class="abs step" style="top:300px"><div class="step__num">3</div><div class="step__title">Geo-Zone Monitoring</div><p class="step__text">Create geo-fenced areas at loading locations to verify and track authorized personnel in real-time.</p></div>
      <div class="abs step" style="top:363px"><div class="step__num">4</div><div class="step__title">Subcontracting Visibility</div><p class="step__text">Maintain full transparency across all subcontracting layers with instant notifications of any changes.</p></div>

      <div class="abs profile">
        <div class="abs profile__head">
          <div class="abs profile__ico"><svg width="24" height="24" viewBox="0 0 24 24"><path d="M6 9h8v6H6zM14 11h3l2 2v2h-5z" fill="#6b7280"/><circle cx="9" cy="16" r="1.3" fill="#6b7280"/><circle cx="16" cy="16" r="1.3" fill="#6b7280"/></svg></div>
          <div class="abs profile__name">Norvik Haulage<br><span style="font-weight:500">Transport &amp; Logistics</span></div>
          <div class="abs chip">Verified</div>
        </div>
        <div class="abs cell" style="left:16px;top:63px"><div class="cell__label">COMPANY DATA</div><div class="cell__val">VAT: 512087346<br>Status: Active</div></div>
        <div class="abs cell" style="left:146px;top:63px"><div class="cell__label">CONTACT</div><div class="cell__val">+48 500 610 720<br>RE410275983316</div></div>
        <div class="abs cell" style="left:16px;top:140px"><div class="cell__label">VERIFICATION</div><div class="cell__val">35 Drivers Verified<br>12 Vehicles Registered</div></div>
        <div class="abs cell" style="left:146px;top:140px"><div class="cell__label">LOCATION</div><div class="cell__val">Plant 1 - Active<br>Geo-fence: Enabled</div></div>
      </div>
    </section>
  </div>

  <!-- Pricing, CTA and footer -->
  <div class="page page--pricing">
    <div class="abs center eyebrow" style="top:45px">PRICING</div>
    <h2 class="abs center h2" style="top:66px">Choose Your Verification Plan</h2>
    <p class="abs center lead" style="top:108px;left:165px;right:170px">Flexible pricing designed to scale with your business. Start with our free plan and upgrade as you grow.</p>

    <div class="plan" style="left:48px;top:169px;width:185px;height:278px;padding-top:22px">
      <div class="plan__name">Starter</div><div class="plan__price">€0</div><div class="plan__per">per month</div>
      <ul class="plan__list"><li><span class="tick">✓</span>Up to 5 company verifications</li><li><span class="tick">✓</span>Basic identity checks</li><li><span class="tick">✓</span>3 geo-zones</li><li><span class="tick">✓</span>Email support</li><li><span class="cross">✕</span>Subcontracting visibility</li></ul>
      <div class="btn btn--green" style="left:52px;top:229px;width:81px;height:28px;font-size:7.5px">Get Started</div>
    </div>
    <div class="plan plan--featured" style="left:246px;top:162px;width:194px;height:292px;padding-top:24px">
      <div class="abs plan__pop">Most Popular</div>
      <div class="plan__name">Professional</div><div class="plan__price">€49</div><div class="plan__per">per month</div>
      <ul class="plan__list" style="padding-left:21px"><li style="height:22.4px"><span class="tick">✓</span>Up to 50 company verifications</li><li style="height:22.4px"><span class="tick">✓</span>Advanced identity checks</li><li style="height:22.4px"><span class="tick">✓</span>25 geo-zones</li><li style="height:22.4px"><span class="tick">✓</span>Priority support</li><li style="height:22.4px"><span class="tick">✓</span>Basic subcontracting visibility</li></ul>
      <div class="btn btn--green" style="left:54px;top:240px;width:85px;height:29px;font-size:7.5px">Get Started</div>
    </div>
    <div class="plan" style="left:454px;top:169px;width:185px;height:278px;padding-top:22px">
      <div class="plan__name">Enterprise</div><div class="plan__price">€149</div><div class="plan__per">per month</div>
      <ul class="plan__list"><li><span class="tick">✓</span>Unlimited company verifications</li><li><span class="tick">✓</span>AI-powered identity verification</li><li><span class="tick">✓</span>Unlimited geo-zones</li><li><span class="tick">✓</span>24/7 dedicated support</li><li><span class="tick">✓</span>Full subcontracting visibility</li></ul>
      <div class="btn btn--green" style="left:52px;top:229px;width:81px;height:28px;font-size:7.5px">Get Started</div>
    </div>

    <section class="abs cta">
      <h2 class="abs center" style="top:53px;font-size:20px;font-weight:700;color:#fff">Ready to Secure Your Logistics Chain?</h2>
      <p class="abs center" style="top:94px;left:100px;right:100px;font-size:8.5px;line-height:14.5px;color:#d3d7df">Join hundreds of companies that trust Keltavo to verify their partners and protect their operations.</p>
      <div class="btn btn--green" style="left:236px;top:143px;width:88px;height:27px;font-size:7.5px">Book a Demo</div>
    </section>

    <footer class="abs footer">
      <div class="abs" style="left:51px;top:43px;width:190px">
        <div class="f-title">Keltavo</div><div class="f-rule"></div>
        <p style="font-size:7.3px;line-height:14px;color:#aab0bd;margin-top:14px">A European startup focused on verifying and confirming the identity of subcontractors in the transport and logistics industry to prevent fraud.</p>
        <div style="display:flex;gap:8px;margin-top:12px"><div class="social"></div><div class="social"></div><div class="social"></div></div>
      </div>
      <div class="abs" style="left:264px;top:43px"><div class="f-title">Platform</div><div class="f-rule"></div><ul class="f-list"><li>Features</li><li>How It Works</li><li>Pricing</li><li>Case Studies</li></ul></div>
      <div class="abs" style="left:383px;top:43px"><div class="f-title">Company</div><div class="f-rule"></div><ul class="f-list"><li>About Us</li><li>Careers</li><li>Blog</li><li>Contact</li></ul></div>
      <div class="abs" style="left:502px;top:43px"><div class="f-title">Contact Us</div><div class="f-rule"></div>
        <ul class="f-list">
          <li><svg width="8" height="6" viewBox="0 0 8 6" style="margin-right:6px"><rect width="8" height="6" fill="#22b573"/><path d="M0 0l4 3 4-3" stroke="#131a2a" fill="none" stroke-width=".8"/></svg>hello@keltavo.com</li>
          <li><svg width="8" height="8" viewBox="0 0 8 8" style="margin-right:6px"><path d="M1 0h2l1 2-1 1a5 5 0 0 0 2 2l1-1 2 1v2c-4 0-8-4-8-7z" fill="#22b573"/></svg>+48 100 200 300</li>
          <li><svg width="6" height="8" viewBox="0 0 6 8" style="margin-right:6px"><path d="M3 0a3 3 0 0 1 3 3c0 2-3 5-3 5S0 5 0 3a3 3 0 0 1 3-3z" fill="#22b573"/></svg>Warsaw, Poland</li>
        </ul>
      </div>
      <div class="abs" style="left:51px;right:51px;top:177px;height:1px;background:#2a3142"></div>
      <p class="abs center" style="top:196px;font-size:6.8px;color:#aab0bd">© 2023 Keltavo. All rights reserved.</p>
    </footer>
  </div>

</div>
</body>
</html>
```